Fernvale Business Card Design

We are looking for a fresh business card design for our new logo. We would like a business card that is unique but friendly. We are in the window coverings business offering blinds, shutters and shades for homes.

Target Market(s)

Targeting the end-consumer

Industry/Entity Type

Business

Requirements
Must have
• Must have a dedicates space for a photo of our sales person. Must contain our new logo (attached).

```html
<!DOCTYPE html>
<html lang="en">
<head>
<meta charset="utf-8">
<title>Fernvale Business Card</title>
<link rel="stylesheet" href="https://fonts.googleapis.com/css2?family=Arimo:wght@400;700&display=swap">
<style>
  :root {
    --page-bg: #23252a;
    --leaf-green: #8bc240;
    --slate-grey: #5f6062;
    --paper-white: #ffffff;
    --map-tint: rgba(120, 175, 55, 0.35);
    --photo-light: #c9ced4;
    --photo-dark: #6d747c;
  }
  * { box-sizing: border-box; margin: 0; padding: 0; }
  html, body {
    width: 1200px; height: 900px; overflow: hidden;
    background: var(--page-bg);
    font-family: "Arimo", Arial, sans-serif;
  }
  .card {
    position: absolute; left: 270px;
    width: 660px; height: 377px; overflow: hidden;
    box-shadow: 0 10px 30px rgba(0,0,0,0.45);
  }
  .card-back { top: 50px; background: var(--leaf-green); }
  .card-front { top: 473px; background: var(--paper-white); }

  .edge-band { position: absolute; top: 0; bottom: 0; width: 52px; background: var(--slate-grey); }
  .edge-band.left { left: 0; }
  .edge-band.right { right: 0; }

  .map-wash {
    position: absolute; left: 90px; top: 40px; width: 480px; height: 290px;
    background: radial-gradient(ellipse at center, var(--map-tint), rgba(139,194,64,0) 70%);
  }

  .brand { position: absolute; display: flex; align-items: center; gap: 18px; }
  .brand-square { width: 62px; height: 62px; border: 4px solid currentColor; border-radius: 8px; }
  .brand-name { font-size: 54px; font-weight: 400; letter-spacing: 1px; line-height: 1; }
  .card-back .brand { color: var(--paper-white); left: 50%; top: 50%; transform: translate(-50%, -50%); }
  .card-front .brand { color: var(--slate-grey); left: 40px; top: 112px; }

  .front-shapes { position: absolute; inset: 0; }

  .photo-frame {
    position: absolute; left: 447px; top: 58px; width: 156px; height: 156px;
    border: 3px solid var(--slate-grey); background: var(--paper-white); padding: 6px;
  }
  .photo-slot {
    width: 100%; height: 100%;
    background: linear-gradient(160deg, var(--photo-light), var(--photo-dark));
  }

  .person { position: absolute; left: 460px; top: 228px; width: 170px; color: var(--paper-white); text-align: center; }
  .person-name { font-size: 22px; font-weight: 700; line-height: 1; }
  .person-role { font-size: 12px; letter-spacing: 1px; margin-top: 2px; }

  .contact-list { position: absolute; left: 40px; top: 258px; list-style: none; color: var(--paper-white); }
  .contact-list li { display: flex; align-items: center; gap: 10px; font-size: 18px; height: 30px; }
  .contact-icon { width: 16px; height: 16px; flex: none; }
</style>
</head>
<body>

<section class="card card-back" aria-label="Card back">
  <div class="edge-band left"></div>
  <div class="edge-band right"></div>
  <div class="map-wash" role="img" aria-label="Faint world map in the background"></div>
  <div class="brand">
    <span class="brand-square"></span>
    <span class="brand-name">Fernvale</span>
  </div>
</section>

<section class="card card-front" aria-label="Card front">
  <svg class="front-shapes" width="660" height="377" viewBox="0 0 660 377" aria-hidden="true">
    <polygon points="0,207 432,207 432,100 660,100 660,377 0,377" fill="var(--leaf-green)"/>
    <polyline points="0,198 424,198 424,91 660,91" fill="none" stroke="var(--slate-grey)" stroke-width="3"/>
  </svg>

  <div class="brand">
    <span class="brand-square"></span>
    <span class="brand-name">Fernvale</span>
  </div>

  <div class="photo-frame">
    <div class="photo-slot" role="img" aria-label="Photo of the sales person"></div>
  </div>

  <div class="person">
    <p class="person-name">YourName</p>
    <p class="person-role">DIRECTOR</p>
  </div>

  <ul class="contact-list">
    <li>
      <svg class="contact-icon" viewBox="0 0 16 16"><rect x="1" y="1" width="14" height="14" rx="2" fill="var(--paper-white)"/><path d="M5 4c1 3 3 6 6 8l1.5-1.5-2-1.5-1 1c-1-.7-2-1.8-2.5-2.8l1-1L6.5 4z" fill="var(--leaf-green)"/></svg>
      <span>000-123-000</span>
    </li>
    <li>
      <svg class="contact-icon" viewBox="0 0 16 16"><rect x="1" y="1" width="14" height="14" rx="2" fill="var(--paper-white)"/><rect x="3.5" y="5" width="9" height="6" fill="none" stroke="var(--leaf-green)" stroke-width="1.2"/><path d="M3.5 5l4.5 3.5L12.5 5" fill="none" stroke="var(--leaf-green)" stroke-width="1.2"/></svg>
      <span>info@fernvale.com</span>
    </li>
    <li>
      <svg class="contact-icon" viewBox="0 0 16 16"><rect x="1" y="1" width="14" height="14" rx="2" fill="var(--paper-white)"/><circle cx="8" cy="8" r="4.5" fill="none" stroke="var(--leaf-green)" stroke-width="1.2"/><path d="M3.5 8h9M8 3.5c-2 2.5-2 6.5 0 9M8 3.5c2 2.5 2 6.5 0 9" fill="none" stroke="var(--leaf-green)" stroke-width="1"/></svg>
      <span>www.fernvale.com</span>
    </li>
  </ul>
</section>

</body>
</html>
```